Business Card Design for Brightkeel

The company provides engineering tender consulting services and personnel resources. The target market is large engineering construction and services companies. The business is based in Australia.

```html
<!DOCTYPE html>
<html lang="en">
<head>
<meta charset="utf-8">
<title>Brightkeel – Business Card</title>
<link rel="stylesheet" href="https://fonts.googleapis.com/css2?family=Open+Sans:wght@400;600;700&display=swap">
<style>
  :root {
    --page-bg: #d9d9d9;
    --card-blue: #2e5d98;
    --card-blue-light: #3d74b3;
    --card-white: #ffffff;
    --lime: #b3d22b;
    --ink: #2b2b2b;
    --ink-soft: #555555;
    --brand-blue: #1f5aa6;
    --on-blue: #ffffff;
  }
  * { box-sizing: border-box; margin: 0; padding: 0; }
  html, body {
    width: 1200px; height: 907px; overflow: hidden;
    background: var(--page-bg);
    font-family: "Open Sans", sans-serif;
  }
  .canvas { position: relative; width: 1200px; height: 907px; }

  .card {
    position: absolute; width: 700px; height: 400px;
    border-radius: 10px; overflow: hidden;
    box-shadow: 0 8px 24px rgba(0,0,0,.25);
  }
  .card__edges { position: absolute; inset: 0; width: 100%; height: 100%; }

  /* Back of card */
  .card--back { left: 290px; top: 40px; background: var(--card-white); }
  .back__brand {
    position: absolute; top: 26px; right: 34px;
    display: flex; align-items: center; gap: 10px;
  }
  .back__brand-name { font-weight: 700; font-size: 22px; color: var(--brand-blue); }
  .back__brand-square { width: 22px; height: 22px; background: var(--lime); }
  .feature-list { position: absolute; left: 44px; top: 118px; list-style: none; }
  .feature-list li {
    display: flex; align-items: center; gap: 12px;
    font-size: 16px; font-weight: 600; color: var(--ink);
    line-height: 29px; white-space: nowrap;
  }
  .feature-list li::before {
    content: ""; width: 0; height: 0;
    border-left: 14px solid var(--brand-blue);
    border-top: 7px solid transparent; border-bottom: 7px solid transparent;
  }
  .feature-list .lead { margin-right: 14px; font-weight: 700; }
  .signatory { position: absolute; right: 38px; bottom: 58px; text-align: right; }
  .signatory__name { font-size: 22px; color: var(--brand-blue); }
  .signatory__role { font-size: 12px; font-weight: 700; color: var(--ink); }

  /* Front of card */
  .card--front {
    left: 200px; top: 470px;
    background: radial-gradient(ellipse at 55% 45%, var(--card-blue-light), var(--card-blue) 70%);
    color: var(--on-blue);
  }
  .front__square {
    position: absolute; left: 110px; top: 130px;
    width: 92px; height: 92px; background: var(--lime);
  }
  .front__name {
    position: absolute; left: 268px; top: 108px;
    font-size: 42px; font-weight: 700; letter-spacing: .5px;
  }
  .contact {
    position: absolute; left: 272px; top: 178px;
    display: grid; grid-template-columns: 130px 28px 1px 28px auto;
    row-gap: 14px; column-gap: 10px; align-items: center;
    font-size: 14px; letter-spacing: .5px;
  }
  .contact__divider { grid-row: span 2; width: 1px; height: 54px; background: rgba(255,255,255,.5); }
  .contact__icon { width: 22px; height: 22px; }
  .reg { position: absolute; left: 272px; top: 262px; font-size: 14px; letter-spacing: .5px; }
  .reg__label { color: var(--lime); margin-right: 10px; }
</style>
</head>
<body>
<main class="canvas">

  <section class="card card--back" aria-label="Business card back">
    <svg class="card__edges" viewBox="0 0 700 400" aria-hidden="true">
      <line x1="40" y1="12" x2="520" y2="12" stroke="var(--lime)" stroke-width="10" stroke-dasharray="30 14"/>
      <polygon points="8,12 40,-4 40,28" fill="var(--lime)"/>
    </svg>
    <div class="back__brand">
      <span class="back__brand-name">Brightkeel</span>
      <span class="back__brand-square"></span>
    </div>
    <ul class="feature-list">
      <li><span class="lead">Your Text is here</span>Your Text is here Your Text is here...</li>
      <li><span class="lead">Your Text is here</span>Your Text is here Your Text is here...</li>
      <li><span class="lead">Your Text is here</span>Your Text is here Your Text is here...</li>
      <li><span class="lead">Your Text is here</span>Your Text is here Your Text is here...</li>
      <li><span class="lead">Your Text is here</span>Your Text is here Your Text is here...</li>
      <li><span class="lead">Your Text is here</span>Your Text is here Your Text is here...</li>
      <li><span class="lead">Your Text is here</span>Your Text is here Your Text is here...</li>
      <li><span class="lead">Your Text is here</span>Your Text is here Your Text is here...</li>
    </ul>
    <div class="signatory">
      <p class="signatory__name">Dana Whitford</p>
      <p class="signatory__role">General Manager</p>
    </div>
  </section>

  <section class="card card--front" aria-label="Business card front">
    <svg class="card__edges" viewBox="0 0 700 400" aria-hidden="true">
      <line x1="0" y1="10" x2="640" y2="10" stroke="var(--on-blue)" stroke-width="10" stroke-dasharray="30 14"/>
      <polygon points="692,10 658,-6 658,26" fill="var(--on-blue)"/>
      <line x1="60" y1="390" x2="700" y2="390" stroke="var(--lime)" stroke-width="10" stroke-dasharray="30 14"/>
      <polygon points="8,390 42,374 42,406" fill="var(--lime)"/>
    </svg>
    <div class="front__square"></div>
    <h1 class="front__name">Brightkeel</h1>
    <div class="contact">
      <span>999 999 999</span>
      <svg class="contact__icon" viewBox="0 0 24 24" aria-label="Mobile"><rect x="7" y="2" width="10" height="20" rx="2" fill="var(--lime)"/><rect x="9" y="5" width="6" height="10" fill="var(--card-blue)"/></svg>
      <span class="contact__divider"></span>
      <svg class="contact__icon" viewBox="0 0 24 24" aria-label="Email"><rect x="2" y="5" width="20" height="14" fill="var(--lime)"/><polyline points="2,5 12,13 22,5" fill="none" stroke="var(--card-blue)" stroke-width="2"/></svg>
      <span>nnnn@nnn.com.au</span>
      <span>999 999 999</span>
      <svg class="contact__icon" viewBox="0 0 24 24" aria-label="Phone"><path d="M3 9 Q12 2 21 9 L18 12 L15 10 L9 10 L6 12 Z" fill="var(--lime)"/><rect x="6" y="12" width="12" height="8" rx="2" fill="var(--lime)"/></svg>
      <svg class="contact__icon" viewBox="0 0 24 24" aria-label="Address"><polygon points="12,3 22,12 19,12 19,21 5,21 5,12 2,12" fill="var(--on-blue)"/><rect x="10" y="15" width="4" height="6" fill="var(--card-blue)"/></svg>
      <span>99,Nnnnnnnnn,Nnn,9999</span>
    </div>
    <p class="reg"><span class="reg__label">RegNo</span>ABN99999999999</p>
  </section>

</main>
</body>
</html>
```